International Career Development Workshop

I need a Powerpoint revised and designed in a more professional manner for a presentation I will be giving. We are an International Education Company that provides students with Internships Abroad, and are expanding our career development programming to offer more guidance through on-site workshops. I am happy to send along our website to showcase the colors and fonts we use, but we tend to use royal blue, lime green, and white in our color scheme. The final design should communicate opportunity and self-awareness within college students.

Target Market(s)

College Students, University Partners, and International Education Community

Industry/Entity Type

Education

Font styles to use
Sans Serif

Colors
9bcb3b
0355a3
ffffff

Requirements
Must have
• Our logo, our color scheme, a unified, professional theme throughout, Watermark of our logo, thematic sections spread across four sections.
Nice to have
• Videos and graphics
Should not have
• Spelling Errors, sloppy design

```html
<!DOCTYPE html>
<html lang="en">
<head>
<meta charset="utf-8">
<title>Horizon Abroad – Career Development Workshop Deck</title>
<link href="https://fonts.googleapis.com/css2?family=Open+Sans:wght@400;600;700&display=swap" rel="stylesheet">
<style>
:root{
  --lime:#9bcb3b;
  --royal:#0355a3;
  --band:#2f74c0;
  --white:#ffffff;
  --ink:#222a33;
  --muted:#5b6470;
  --stage:#000000;
  --photo-a:#c9a78c;
  --photo-b:#5d6f8a;
}
*{box-sizing:border-box;margin:0;padding:0}
html,body{width:1189px;height:1200px;overflow:hidden;background:var(--stage)}
body{position:relative;font-family:"Open Sans",Arial,sans-serif;color:var(--ink)}
.slide{position:absolute;width:352px;height:212px;background:var(--white);overflow:hidden}
.col-1{left:53px}.col-2{left:427px}.col-3{left:803px}
.row-1{top:112px}.row-2{top:370px}.row-3{top:629px}.row-4{top:887px}
.footer-bar{position:absolute;left:0;right:0;bottom:0;height:8px;display:flex}
.footer-bar span{flex:1}
.footer-bar .green{background:var(--lime)}
.footer-bar .blue{background:var(--royal)}
.page-tab{position:absolute;right:3px;top:10px;width:9px;height:28px;background:var(--lime);border-bottom:2px solid var(--royal)}
.page-tab span{position:absolute;left:50%;top:50%;transform:translate(-50%,-50%) rotate(90deg);font-size:5px;color:var(--white);white-space:nowrap}
.slide-title{position:absolute;font-size:13px;font-weight:700;color:var(--royal);letter-spacing:.1px}
.photo{position:absolute;background:linear-gradient(160deg,var(--photo-a),var(--photo-b))}
.body-copy{position:absolute;font-size:5.6px;line-height:7.2px;color:var(--ink);text-align:justify}
.brand{display:flex;align-items:center;gap:6px;color:var(--royal);font-weight:700}
.brand .dot{border-radius:50%;background:var(--royal)}
/* title slide */
.title-band{position:absolute;left:0;right:0;top:121px;height:64px;background:var(--band)}
.title-band .main{position:absolute;left:188px;width:140px;top:9px;text-align:center;color:var(--white);font-size:12px;line-height:17px}
.title-band .sub{position:absolute;left:188px;width:140px;top:48px;text-align:center;color:var(--white);font-size:6px}
/* welcome */
.welcome{position:absolute;left:0;right:0;top:98px;text-align:center}
.welcome .kicker{font-size:10px;color:var(--lime);letter-spacing:.5px}
.welcome .headline{font-size:14px;font-weight:600;color:var(--royal);margin-top:2px}
.welcome .rule{width:106px;height:1px;background:var(--royal);margin:8px auto 0;position:relative}
.welcome .rule::after{content:"";position:absolute;left:40px;width:26px;top:-1px;border-top:2px dotted var(--lime)}
/* lists */
.agenda{position:absolute;left:33px;top:52px;list-style:none}
.agenda li{font-size:8px;height:16.2px;display:flex;align-items:center;gap:9px}
.agenda .badge{width:7px;height:8px;background:var(--lime);border-radius:1px 1px 3px 3px}
.services{position:absolute;left:212px;top:36px;list-style:none}
.services li{font-size:7px;height:15.9px;display:flex;align-items:center;gap:6px}
.services svg{width:6px;height:6px}
/* columns */
.col-head{position:absolute;font-size:8px;font-weight:700;text-align:center}
/* team */
.member{position:absolute;top:60px;width:74px;text-align:center}
.member .frame{width:74px;height:74px;border:3px solid #e8e8e8;box-shadow:0 1px 3px rgba(0,0,0,.3);position:relative}
.member .frame .photo{inset:0}
.member .name{font-size:7.5px;margin-top:7px}
.member .role{font-size:4.5px;color:var(--muted);margin-top:2px}
/* contact */
.contact{position:absolute;left:193px;top:128px;border-left:2px solid var(--lime);padding-left:8px;font-size:7px;line-height:10.5px}
.contact .gap{height:6px}
.contact a{color:#1a3fd6;text-decoration:underline}
/* thank you */
.thanks-panel{position:absolute;left:179px;top:0;right:0;bottom:0;background:var(--band)}
.thanks-panel h2{position:absolute;left:0;right:0;top:70px;text-align:center;color:var(--white);font-size:24px;font-weight:700}
.thanks-panel .brand{position:absolute;left:54px;top:116px;color:var(--white);font-size:8px}
.thanks-panel .brand .dot{background:var(--white)}
</style>
</head>
<body>

<!-- Row 1 -->
<section class="slide col-1 row-1">
  <div class="photo" style="left:20px;top:18px;width:140px;height:194px;border-radius:60px 60px 0 0" role="img" aria-label="Photo of a smiling student holding books"></div>
  <div class="brand" style="position:absolute;left:184px;top:38px;font-size:14px"><span class="dot" style="width:16px;height:16px"></span>HORIZON ABROAD</div>
  <div class="title-band">
    <p class="main">Click to Edit Your Business Title Style</p>
    <p class="sub">Click to Edit Your Subtitle Style</p>
  </div>
</section>

<section class="slide col-2 row-1">
  <div class="welcome">
    <p class="kicker">WELCOME</p>
    <p class="headline">OUR PRESENTATION</p>
    <div class="rule"></div>
  </div>
</section>

<section class="slide col-3 row-1">
  <h2 class="slide-title" style="left:31px;top:16px">Presentation Agenda</h2>
  <ul class="agenda">
    <li><span class="badge"></span>About US</li>
    <li><span class="badge"></span>Our Mission</li>
    <li><span class="badge"></span>What We Do</li>
    <li><span class="badge"></span>Dividing Slide</li>
    <li><span class="badge"></span>Our Team</li>
    <li><span class="badge"></span>What Do You Choose US</li>
    <li><span class="badge"></span>Our Chart Area</li>
    <li><span class="badge"></span>Contact US</li>
  </ul>
  <div class="photo" style="left:210px;top:16px;width:140px;height:188px;border-radius:50px 50px 0 0" role="img" aria-label="Photo of a smiling graduate in cap and gown"></div>
  <div class="footer-bar"><span class="green"></span><span class="blue"></span></div>
</section>

<!-- Row 2 -->
<section class="slide col-1 row-2">
  <h2 class="slide-title" style="left:30px;top:16px">About US</h2>
  <p class="body-copy" style="left:30px;top:72px;width:140px">Our workshops help students turn time abroad into clear career direction. Through guided reflection, skill mapping and mentoring, every participant leaves with a sharper sense of strengths, goals and next steps. We partner with universities and host employers to build programs that match real workplace needs and local culture.</p>
  <div class="photo" style="left:184px;top:0;width:168px;height:204px;clip-path:polygon(28% 0,100% 0,100% 100%,0 100%)" role="img" aria-label="Photo of a student choosing books in a library"></div>
  <div class="page-tab"><span>Page 1</span></div>
  <div class="footer-bar"><span class="green"></span><span class="blue"></span></div>
</section>

<section class="slide col-2 row-2">
  <h2 class="slide-title" style="left:30px;top:16px">Our Mission</h2>
  <p class="body-copy" style="left:30px;top:47px;width:155px">We help college students discover who they are and where they can go, combining international internships with on-site career workshops that build confidence, self-awareness and lasting professional skills.</p>
  <div class="photo" style="left:188px;top:40px;width:164px;height:164px;border-radius:40px 40px 0 0" role="img" aria-label="Photo of two cheering students holding colourful folders in the air"></div>
  <div class="page-tab"><span>Page 2</span></div>
  <div class="footer-bar"><span class="green"></span><span class="blue"></span></div>
</section>

<section class="slide col-3 row-2">
  <h2 class="slide-title" style="left:30px;top:16px">What We Do</h2>
  <div class="photo" style="left:8px;top:58px;width:170px;height:146px;border-radius:40px 40px 0 0" role="img" aria-label="Photo of a group of students reading, one holding a red folder"></div>
  <ul class="services">
    <li><svg viewBox="0 0 6 6"><path d="M.5 3.2 2.3 5 5.5 1" fill="none" stroke="#9bcb3b" stroke-width="1"/></svg>Sealants</li>
    <li><svg viewBox="0 0 6 6"><path d="M.5 3.2 2.3 5 5.5 1" fill="none" stroke="#9bcb3b" stroke-width="1"/></svg>Root Canal Therapy</li>
    <li><svg viewBox="0 0 6 6"><path d="M.5 3.2 2.3 5 5.5 1" fill="none" stroke="#9bcb3b" stroke-width="1"/></svg>Extractions</li>
    <li><svg viewBox="0 0 6 6"><path d="M.5 3.2 2.3 5 5.5 1" fill="none" stroke="#9bcb3b" stroke-width="1"/></svg>Scaling and Root Planing</li>
    <li><svg viewBox="0 0 6 6"><path d="M.5 3.2 2.3 5 5.5 1" fill="none" stroke="#9bcb3b" stroke-width="1"/></svg>Implant Retained Dentures</li>
    <li><svg viewBox="0 0 6 6"><path d="M.5 3.2 2.3 5 5.5 1" fill="none" stroke="#9bcb3b" stroke-width="1"/></svg>Sleep Apnea Treatment</li>
    <li><svg viewBox="0 0 6 6"><path d="M.5 3.2 2.3 5 5.5 1" fill="none" stroke="#9bcb3b" stroke-width="1"/></svg>Snoring Treatment</li>
    <li><svg viewBox="0 0 6 6"><path d="M.5 3.2 2.3 5 5.5 1" fill="none" stroke="#9bcb3b" stroke-width="1"/></svg>Maxillofacial Surgery</li>
    <li><svg viewBox="0 0 6 6"><path d="M.5 3.2 2.3 5 5.5 1" fill="none" stroke="#9bcb3b" stroke-width="1"/></svg>Laser Dentistry</li>
  </ul>
  <div class="page-tab"><span>Page 3</span></div>
  <div class="footer-bar"><span class="green"></span><span class="blue"></span></div>
</section>

<!-- Row 3 -->
<section class="slide col-1 row-3">
  <h2 class="slide-title" style="left:26px;top:16px">Dividing Slide</h2>
  <p class="col-head" style="left:26px;top:45px;width:138px">Sample Text</p>
  <p class="col-head" style="left:183px;top:45px;width:138px">Sample Text</p>
  <p class="body-copy" style="left:26px;top:62px;width:138px">Our workshops help students turn time abroad into clear career direction. Through guided reflection, skill mapping and mentoring, every participant leaves with a sharper sense of strengths, goals and next steps. We partner with universities and host employers to build programs that match real workplace needs and local culture.</p>
  <p class="body-copy" style="left:183px;top:62px;width:138px">Our workshops help students turn time abroad into clear career direction. Through guided reflection, skill mapping and mentoring, every participant leaves with a sharper sense of strengths, goals and next steps. We partner with universities and host employers to build programs that match real workplace needs and local culture.</p>
  <div class="page-tab"><span>Page 4</span></div>
  <div class="footer-bar"><span class="green"></span><span class="blue"></span></div>
</section>

<section class="slide col-2 row-3">
  <h2 class="slide-title" style="left:39px;top:14px">Our Team</h2>
  <div class="member" style="left:46px"><div class="frame"><div class="photo" role="img" aria-label="Portrait of a team member in a suit"></div></div><p class="name">Alex Moore</p><p class="role">Principal</p></div>
  <div class="member" style="left:138px"><div class="frame"><div class="photo" role="img" aria-label="Portrait of a team member in a suit"></div></div><p class="name">Daniel Reed</p><p class="role">Principal</p></div>
  <div class="member" style="left:232px"><div class="frame"><div class="photo" role="img" aria-label="Portrait of a team member in a blazer"></div></div><p class="name">Nina Park</p><p class="role">Principal</p></div>
  <div class="page-tab"><span>Page 5</span></div>
  <div class="footer-bar"><span class="green"></span><span class="blue"></span></div>
</section>

<section class="slide col-3 row-3">
  <h2 class="slide-title" style="left:30px;top:16px">What Do You Choose Us</h2>
  <p class="body-copy" style="left:30px;top:66px;width:275px">Students gain hands-on experience with global employers while our coaches guide them to reflect on each placement. Every workshop links daily tasks to long-term goals, so growth abroad becomes a story they can share with confidence.</p>
  <p class="body-copy" style="left:30px;top:127px;width:275px">University partners receive clear reports on outcomes, and alumni join a network that supports them long after they return home.</p>
  <div class="page-tab"><span>Page 6</span></div>
  <div class="footer-bar"><span class="green"></span><span class="blue"></span></div>
</section>

<!-- Row 4 -->
<section class="slide col-1 row-4">
  <h2 class="slide-title" style="left:29px;top:15px">Our Chart Area</h2>
  <svg style="position:absolute;left:0;top:0" width="352" height="212" viewBox="0 0 352 212" role="img" aria-label="Line chart of three series across four categories">
    <g font-family="Open Sans, sans-serif" font-size="7" fill="#222">
      <g stroke="#c8c8c8" stroke-width=".6">
        <line x1="86" y1="51" x2="230" y2="51"/><line x1="86" y1="67.5" x2="230" y2="67.5"/>
        <line x1="86" y1="84" x2="230" y2="84"/><line x1="86" y1="100.5" x2="230" y2="100.5"/>
        <line x1="86" y1="117" x2="230" y2="117"/><line x1="86" y1="133.5" x2="230" y2="133.5"/>
      </g>
      <line x1="86" y1="150" x2="230" y2="150" stroke="#888" stroke-width=".8"/>
      <line x1="86" y1="51" x2="86" y2="150" stroke="#888" stroke-width=".8"/>
      <text x="75" y="153">0</text><text x="75" y="136.5">1</text><text x="75" y="120">2</text>
      <text x="75" y="103.5">3</text><text x="75" y="87">4</text><text x="75" y="70.5">5</text><text x="75" y="54">6</text>
      <g text-anchor="middle">
        <text x="104" y="162">Category</text><text x="104" y="171">1</text>
        <text x="140" y="162">Category</text><text x="140" y="171">2</text>
        <text x="176" y="162">Category</text><text x="176" y="171">3</text>
        <text x="212" y="162">Category</text><text x="212" y="171">4</text>
      </g>
      <polyline points="104,79 140,108.8 176,92.3 212,75.8" fill="none" stroke="#2f6fc0" stroke-width="1"/>
      <polyline points="104,110.4 140,77.4 176,120.3 212,103.8" fill="none" stroke="#9bcb3b" stroke-width="1"/>
      <polyline points="104,117 140,117 176,100.5 212,67.5" fill="none" stroke="#000" stroke-width="1"/>
      <g fill="#2f6fc0"><circle cx="104" cy="79" r="1.4"/><circle cx="140" cy="108.8" r="1.4"/><circle cx="176" cy="92.3" r="1.4"/><circle cx="212" cy="75.8" r="1.4"/></g>
      <g fill="#9bcb3b"><rect x="102.6" y="109" width="2.8" height="2.8"/><rect x="138.6" y="76" width="2.8" height="2.8"/><rect x="174.6" y="118.9" width="2.8" height="2.8"/><rect x="210.6" y="102.4" width="2.8" height="2.8"/></g>
      <g fill="#000"><path d="M104 115.4l1.6 2.4h-3.2z"/><path d="M140 115.4l1.6 2.4h-3.2z"/><path d="M176 98.9l1.6 2.4h-3.2z"/><path d="M212 65.9l1.6 2.4h-3.2z"/></g>
      <line x1="240" y1="99" x2="252" y2="99" stroke="#2f6fc0"/><circle cx="246" cy="99" r="1.3" fill="#2f6fc0"/><text x="254" y="101.5">Series 1</text>
      <line x1="240" y1="112.5" x2="252" y2="112.5" stroke="#9bcb3b"/><rect x="244.6" y="111.1" width="2.8" height="2.8" fill="#9bcb3b"/><text x="254" y="115">Series 2</text>
      <line x1="240" y1="126" x2="252" y2="126" stroke="#000"/><path d="M246 124.6l1.6 2.4h-3.2z"/><text x="254" y="128.5">Series 3</text>
    </g>
  </svg>
  <div class="page-tab"><span>Page 7</span></div>
  <div class="footer-bar"><span class="green"></span><span class="blue"></span></div>
</section>

<section class="slide col-2 row-4">
  <div class="brand" style="position:absolute;left:192px;top:32px;font-size:11.5px"><span class="dot" style="width:14px;height:14px"></span>HORIZON ABROAD</div>
  <h2 class="slide-title" style="left:190px;top:98px">Contact US</h2>
  <div class="contact">
    <p>Address:</p>
    <p>48 Harbor Lane, Boston, USA</p>
    <div class="gap"></div>
    <p>Tel: +1 (000) 000-0000</p>
    <p>Email: <a>hello@horizonabroad.org</a></p>
    <p>Web: www.horizonabroad.org</p>
  </div>
  <div class="photo" style="left:0;top:62px;width:178px;height:142px;border-radius:0 50px 0 0" role="img" aria-label="Photo of two students reading notebooks together"></div>
  <div class="page-tab"><span>Page 8</span></div>
  <div class="footer-bar"><span class="green"></span><span class="blue"></span></div>
</section>

<section class="slide col-3 row-4">
  <div class="brand" style="position:absolute;left:14px;top:96px;font-size:12px"><span class="dot" style="width:16px;height:16px"></span>HORIZON<br>ABROAD</div>
  <div class="thanks-panel">
    <h2>THANK YOU</h2>
    <div class="brand"><span class="dot" style="width:10px;height:10px"></span>HORIZON ABROAD</div>
  </div>
</section>

</body>
</html>
```